Salon website

Need a web design for a new blow dry and hair extension boutique in CT
would like the color scheme to be gray, white and tiffany blue
Create a web site with about 4 pages showing
1 about us page
1 blow dry services page
1 hair extension services page
1 contact us page
1 membership page
1 parties page

Industry/Entity Type

Boutique

Colors
86cfc6
cfeae6
33b7a4
aaaaaa
cbcbcb
ffffff

```html
<!DOCTYPE html>
<html lang="en">
<head>
<meta charset="utf-8">
<title>Blow Dry and Hair Extension Boutique</title>
<link rel="stylesheet" href="https://fonts.googleapis.com/css2?family=PT+Sans:ital,wght@0,400;0,700;1,400&display=swap">
<style>
  :root {
    --white: #ffffff;
    --ink: #1f1f1f;
    --heading-grey: #6b6b6b;
    --muted-grey: #6e6e6e;
    --nav-active: #5c5c5c;
    --panel-white: rgba(250, 248, 246, 0.88);
    --teal: rgba(12, 148, 138, 0.92);
    --footer-band: #e6e6e6;
    --hair-dark: #2a231f;
    --hair-gold: #c98b4a;
    --hair-light: #e3b77c;
    --hair-brown: #5a3a22;
  }
  * { margin: 0; padding: 0; box-sizing: border-box; }
  html, body {
    width: 1200px;
    height: 989px;
    overflow: hidden;
    background: var(--white);
    font-family: "PT Sans", Arial, sans-serif;
  }
  .page { position: relative; width: 1200px; height: 989px; }

  .hero-photo {
    position: absolute; left: 0; top: 0; width: 1200px; height: 820px;
    background:
      radial-gradient(ellipse 340px 480px at 470px 470px, rgba(240,200,150,0.9), rgba(240,200,150,0) 70%),
      radial-gradient(ellipse 420px 620px at 480px 420px, var(--hair-light), rgba(201,139,74,0.0) 75%),
      radial-gradient(ellipse 560px 700px at 460px 460px, var(--hair-gold), rgba(90,58,34,0) 80%),
      linear-gradient(180deg, var(--hair-dark) 0%, #3a2b22 40%, var(--hair-brown) 100%);
  }

  .intro-panel {
    position: absolute; left: 0; top: 206px; width: 616px; height: 327px;
    background: var(--panel-white);
  }
  .intro-title {
    position: absolute; left: 230px; top: 190px;
    font-size: 39px; font-weight: 700; line-height: 1;
    color: var(--heading-grey); letter-spacing: -0.3px;
  }
  .intro-copy {
    position: absolute; left: 280px; top: 247px; width: 312px;
    font-size: 13.6px; line-height: 18.4px; color: var(--ink);
  }
  .intro-copy p + p { margin-top: 18.4px; }

  .brand-panel {
    position: absolute; left: 643px; top: 206px; width: 325px; height: 130px;
    background: var(--teal);
  }
  .brand-title {
    position: absolute; left: 648px; top: 193px;
    font-size: 39px; font-weight: 700; line-height: 36px;
    color: var(--white); text-transform: uppercase; letter-spacing: -0.3px;
  }
  .main-nav {
    position: absolute; left: 654px; top: 318px;
    display: flex; gap: 19px; list-style: none;
    font-size: 13.6px; line-height: 18px;
  }
  .main-nav a { color: var(--white); text-decoration: none; }
  .main-nav a.is-active { color: var(--nav-active); font-weight: 700; }

  .site-footer {
    position: absolute; left: 0; top: 858px; width: 613px; height: 131px;
    background: var(--footer-band);
  }
  .footer-col {
    position: absolute; top: 870px;
    font-size: 13.6px; color: var(--muted-grey);
  }
  .footer-col h2 { font-size: 13.6px; font-weight: 400; line-height: 18px; margin-bottom: 9px; }
  .footer-col ul { list-style: none; font-style: italic; line-height: 14.6px; }
  .footer-col li.gap { margin-top: 14.6px; }
  .footer-col a { color: inherit; text-decoration: none; }
  .footer-services { left: 279px; }
  .footer-location { left: 439px; }
</style>
</head>
<body>
<div class="page">
  <div class="hero-photo" role="img" aria-label="Portrait photograph of a woman with long, voluminous golden waves against a dark brown backdrop"></div>

  <div class="intro-panel"></div>
  <h1 class="intro-title">HAIR EXTENSION</h1>
  <div class="intro-copy">
    <p>Indulge your self with our personal touch, exceptional expertise and imaginative innovation at our Salon in CT. We offer a personal, friendly approach to styling, coloring and cutting your hair.</p>
    <p>Besides the basics, we have products that will improve the condition and texture of your hair with results that will amaze you. Our highly trained staff of stylists and master colorists are at the forefront of today's color and cut techniques. To match their skill, we use only the best hair treatment products. Our stylists use true techniques as the foundation of their craft, while constantly searching for the new and improved processes.</p>
  </div>

  <div class="brand-panel"></div>
  <div class="brand-title">Blow Dry and<br>Hair Extension<br>Boutique</div>
  <ul class="main-nav">
    <li><a href="#">About us</a></li>
    <li><a href="#">Bow Dry</a></li>
    <li><a href="#" class="is-active">Hair Extention</a></li>
    <li><a href="#">Contact us</a></li>
  </ul>

  <footer class="site-footer"></footer>
  <div class="footer-col footer-services">
    <h2>Services</h2>
    <ul>
      <li><a href="#">Bow Dry</a></li>
      <li><a href="#">Hair Extensions</a></li>
      <li class="gap"><a href="#">About Us</a></li>
      <li><a href="#">Contact Us</a></li>
    </ul>
  </div>
  <div class="footer-col footer-location">
    <h2>Where to find us</h2>
    <ul>
      <li>1800 55 41 72</li>
      <li class="gap">Level 3,</li>
      <li>18 Fern Lane, Maple Heights,</li>
      <li>Sydney, Australia.</li>
    </ul>
  </div>
</div>
</body>
</html>
```